Design 1 form and 3 panels for shopping App

This goal of this project is to enhance the design of our “internal shopping” web application. We call it “qOrderly”. qOrderly allows an employee to requisition material or services. The user fills a shopping cart and “checks out” in a manner similar to Bramwick or any other consumer site.
The task is to redesign the main shopping form and three “pull out” panels. We are looking for a clean, contemporary design consistent with our branding. Our goal is to make the shopping experience as close as possible to what a user experiences on consumer sites (e.g. Bramwick, Quillet, Farrow Yard). A new user should be able to shop and check out without any training. Therefore, it is important that the shopping experience be familiar to the user.
Updates

Target Market(s)

Mid to large sized companies (> 50M USD Sales per Year)

Industry/Entity Type

Shopping

Number of Pages Required

4 page

Requirements
Must have
• Must look good in the current menu frame.

Files

```html
<!DOCTYPE html>
<html lang="en">
<head>
<meta charset="utf-8">
<title>qOrderly – Request Material</title>
<link href="https://fonts.googleapis.com/css2?family=Open+Sans:wght@400;600;700&display=swap" rel="stylesheet">
<style>
:root{
  --green:#74b93b;
  --black:#000;
  --navy:#0c3b8f;
  --title:#173f8f;
  --orange:#e2660c;
  --yellow:#f6e27a;
  --yellow-edge:#d8c150;
  --card:#f2f2f2;
  --card-edge:#d6d6d6;
  --text:#333;
  --footer:#f2f2f2;
}
*{box-sizing:border-box;margin:0;padding:0}
html,body{width:1200px;height:1063px;overflow:hidden;background:#fff;font-family:'Open Sans',sans-serif;color:var(--text)}
.topbar{height:33px;background:var(--black);color:#fff;font-size:9.5px;position:relative}
.topbar .user{position:absolute;left:99px;top:11px}
.topbar .role{position:absolute;left:268px;top:11px}
.topbar .links{position:absolute;right:99px;top:11px;display:flex;gap:18px}
.topbar .links span.sep{color:#aaa}
.header{position:relative;height:76px}
.tabs{position:absolute;left:99px;top:41px;display:flex;gap:3px}
.tab{height:35px;border:1px solid #ccc;border-bottom:none;background:#fff;font-size:11px;font-weight:700;color:#1a1a2e;display:flex;align-items:center;justify-content:center}
.tab.active{background:var(--green);color:#fff;border-color:var(--green)}
.brand{position:absolute;right:99px;top:28px;font-size:24px;font-weight:700;color:var(--navy)}
.subnav{height:36px;background:var(--green);padding-left:99px;display:flex;align-items:center;color:#fff;font-size:11px}
.subnav .bullet{margin:0 14px;font-size:9px}
.page{width:1002px;margin-left:99px}
.toolbar{position:relative;height:36px;margin-top:28px}
.tool{position:absolute;top:0;height:36px;background:var(--yellow);border:1px solid var(--yellow-edge);font-size:12px;color:#333;display:flex;align-items:center;padding-left:15px}
.tool .caret{position:absolute;right:10px;top:15px;width:0;height:0;border-left:5px solid transparent;border-right:5px solid transparent;border-top:6px solid #333}
.tool.icon{justify-content:center;padding:0}
.search{position:absolute;top:0;left:162px;width:253px;height:36px;background:#f0f0f0;border:1px solid #ccc;font-size:12px;color:#444;display:flex;align-items:center;padding-left:15px}
.badge{position:absolute;top:2px;width:12px;height:12px;border-radius:50%;background:#4caf50;color:#fff;font-size:8px;text-align:center;line-height:12px}
.section-head{height:39px;background:var(--green);margin-top:26px;display:flex;align-items:center;justify-content:space-between;padding:0 5px 0 19px}
.section-head h2{color:#fff;font-size:13.5px;font-weight:700}
.view-all{height:27px;width:73px;background:linear-gradient(#fff,#e2e2e2);border:1px solid #ccc;border-radius:2px;font-size:9.5px;font-weight:700;color:#222;display:flex;align-items:center;justify-content:center}
.grid{display:grid;grid-template-columns:repeat(5,186px);column-gap:18px;margin-top:23px}
.card{height:279px;background:var(--card);border:1px solid var(--card-edge);padding:15px 15px 0;text-align:center}
.photo{height:132px;background:#fff;border:1px solid #ddd;padding:14px}
.photo div{width:100%;height:100%;border-radius:3px}
.card h3{font-size:11px;font-weight:700;color:var(--title);margin-top:18px}
.price{font-size:13px;margin-top:10px;color:#444}
.price b{color:var(--orange)}
.stock{font-size:12px;margin-top:6px;color:#333}
.buy{display:flex;justify-content:space-between;margin-top:12px}
.qty{width:62px;height:28px;background:#fff;border:1px solid #ccc;font-size:11px;position:relative;text-align:left;padding:6px 0 0 10px}
.qty::after{content:"";position:absolute;right:9px;top:11px;border-left:5px solid transparent;border-right:5px solid transparent;border-top:6px solid #333}
.add{width:86px;height:28px;background:var(--navy);color:#fff;font-size:11px;display:flex;align-items:center;justify-content:center;border-radius:2px}
.footer{position:absolute;left:0;top:987px;width:1200px;height:76px;background:var(--footer);border-top:1px solid #e4e4e4;font-size:11.5px;color:#333}
.footer .legal{position:absolute;left:99px;top:29px;display:flex;gap:14px}
.footer .social{position:absolute;right:99px;top:21px;display:flex;align-items:center;gap:8px}
.footer .social .c{width:27px;height:27px;border-radius:50%}
</style>
</head>
<body>
<div class="topbar">
  <span class="user">LOGGED IN AS DANA REYES</span>
  <span class="role">CURRENT ROLE STAFF</span>
  <div class="links"><span>TOUCH</span><span class="sep">|</span><span>NEW TAB</span><span class="sep">|</span><span>HELP</span><span class="sep">|</span><span>SUPPORT</span><span class="sep">|</span><span>LOG OUT</span></div>
</div>
<div class="header">
  <nav class="tabs">
    <div class="tab" style="width:89px">HOME</div>
    <div class="tab active" style="width:157px">REQUEST MATERIAL</div>
    <div class="tab" style="width:156px">REPORT EXPENSES</div>
    <div class="tab" style="width:157px">APPROVE DOCUMENTS</div>
  </nav>
  <div class="brand">Catapulta</div>
</div>
<div class="subnav">
  <span>ENTER A REQUISITION</span><span class="bullet">●</span><span>OTHER TRANSACTIONS</span><span class="bullet">●</span><span>REQUEST HISTORY</span><span class="bullet">●</span><span>PURCHASE HISTORY</span><span class="bullet">●</span><span>YOUR PROFILE</span>
</div>
<main class="page">
  <div class="toolbar">
    <div class="tool" style="left:0;width:108px">Catalog<span class="caret"></span></div>
    <div class="tool icon" style="left:120px;width:39px"><svg width="14" height="14" viewBox="0 0 14 14"><circle cx="6" cy="6" r="4.3" fill="none" stroke="#222" stroke-width="2"/><line x1="9" y1="9" x2="13" y2="13" stroke="#222" stroke-width="2.4"/></svg></div>
    <div class="search">Enter product discription</div>
    <div class="tool icon" style="left:420px;width:39px"><svg width="12" height="12"><rect x="5" y="0" width="2.4" height="12" fill="#222"/><rect x="0" y="5" width="12" height="2.4" fill="#222"/></svg></div>
    <div class="tool" style="left:488px;width:108px;padding-left:12px"><span class="badge" style="left:18px">3</span><svg width="12" height="14" style="margin-right:4px"><rect x="1" y="1" width="10" height="12" fill="none" stroke="#222" stroke-width="1.4"/><line x1="3" y1="5" x2="9" y2="5" stroke="#222"/><line x1="3" y1="8" x2="9" y2="8" stroke="#222"/></svg>My List<span class="caret"></span></div>
    <div class="tool" style="left:604px;width:125px">Market Place<span class="caret"></span></div>
    <div class="tool icon" style="left:737px;width:39px"><svg width="16" height="12" viewBox="0 0 16 12"><path d="M6 1 L1 5.5 L6 10 V7 C10 7 13 8 15 11 C14 6 11 4 6 4 Z" fill="#222"/></svg></div>
    <div class="tool" style="left:894px;width:108px;padding-left:12px"><span class="badge" style="left:23px">3</span><svg width="15" height="13" style="margin-right:4px" viewBox="0 0 15 13"><path d="M0 1 H3 L5 9 H13 L14.5 3 H4" fill="none" stroke="#222" stroke-width="1.6"/><circle cx="6" cy="11.5" r="1.3" fill="#222"/><circle cx="12" cy="11.5" r="1.3" fill="#222"/></svg>Cart<span class="caret"></span></div>
  </div>

  <div class="section-head"><h2>RECENT PRODUCTS</h2><div class="view-all">VIEW ALL</div></div>
  <div class="grid">
    <div class="card"><div class="photo"><div role="img" aria-label="Inkjet printer product photo" style="background:linear-gradient(#3a3a3a 30%,#d8d8d8 30%)"></div></div><h3>WOODEN EXECUTIVE DESK</h3><p class="price">PRICE : <b>$100.00</b></p><p class="stock">Not Inventoried</p><div class="buy"><div class="qty">1</div><div class="add">Add to cart</div></div></div>
    <div class="card"><div class="photo"><div role="img" aria-label="Laptop product photo" style="background:linear-gradient(135deg,#2a1a3a,#a04c9a 55%,#cfcfcf 56%)"></div></div><h3>WOODEN EXECUTIVE DESK</h3><p class="price">PRICE : <b>$100.00</b></p><p class="stock">Not Inventoried</p><div class="buy"><div class="qty">1</div><div class="add">Add to cart</div></div></div>
    <div class="card"><div class="photo"><div role="img" aria-label="Microwave oven product photo" style="background:linear-gradient(90deg,#2e2e2e 75%,#9a9a9a 75%)"></div></div><h3>WOODEN EXECUTIVE DESK</h3><p class="price">PRICE : <b>$100.00</b></p><p class="stock">Not Inventoried</p><div class="buy"><div class="qty">1</div><div class="add">Add to cart</div></div></div>
    <div class="card"><div class="photo"><div role="img" aria-label="Vacuum cleaner product photo" style="background:linear-gradient(160deg,#fff 40%,#f2d21a 60%,#333)"></div></div><h3>WOODEN EXECUTIVE DESK</h3><p class="price">PRICE : <b>$100.00</b></p><p class="stock">Not Inventoried</p><div class="buy"><div class="qty">1</div><div class="add">Add to cart</div></div></div>
    <div class="card"><div class="photo"><div role="img" aria-label="Wooden chest of drawers product photo" style="background:linear-gradient(#7a2612,#4a1408)"></div></div><h3>WOODEN EXECUTIVE DESK</h3><p class="price">PRICE : <b>$100.00</b></p><p class="stock">Not Inventoried</p><div class="buy"><div class="qty">1</div><div class="add">Add to cart</div></div></div>
  </div>

  <div class="section-head" style="margin-top:27px"><h2>POPULAR CATEGORIES</h2><div class="view-all">VIEW ALL</div></div>
  <div class="grid">
    <div class="card"><div class="photo"><div role="img" aria-label="Janitorial cart product photo" style="background:linear-gradient(#fff,#f0c419 50%,#2a2a2a)"></div></div><h3>WOODEN EXECUTIVE DESK</h3><p class="price">PRICE : <b>$100.00</b></p><p class="stock">Not Inventoried</p><div class="buy"><div class="qty">1</div><div class="add">Add to cart</div></div></div>
    <div class="card"><div class="photo"><div role="img" aria-label="Black microwave oven product photo" style="background:linear-gradient(#fff 15%,#0d0d0d 15%,#111 85%,#fff 85%)"></div></div><h3>WOODEN EXECUTIVE DESK</h3><p class="price">PRICE : <b>$100.00</b></p><p class="stock">Not Inventoried</p><div class="buy"><div class="qty">1</div><div class="add">Add to cart</div></div></div>
    <div class="card"><div class="photo"><div role="img" aria-label="Photo printer product photo" style="background:linear-gradient(#fff 10%,#1c1c1c 40%,#3a6b2a 90%)"></div></div><h3>WOODEN EXECUTIVE DESK</h3><p class="price">PRICE : <b>$100.00</b></p><p class="stock">Not Inventoried</p><div class="buy"><div class="qty">1</div><div class="add">Add to cart</div></div></div>
    <div class="card"><div class="photo"><div role="img" aria-label="Notebook computer product photo" style="background:linear-gradient(#1a5aa8,#5fb0e8 65%,#555 66%)"></div></div><h3>WOODEN EXECUTIVE DESK</h3><p class="price">PRICE : <b>$100.00</b></p><p class="stock">Not Inventoried</p><div class="buy"><div class="qty">1</div><div class="add">Add to cart</div></div></div>
    <div class="card"><div class="photo"><div role="img" aria-label="Oak media cabinet product photo" style="background:linear-gradient(#fff 15%,#c79a5e 15%,#8a6436 85%,#fff 85%)"></div></div><h3>WOODEN EXECUTIVE DESK</h3><p class="price">PRICE : <b>$100.00</b></p><p class="stock">Not Inventoried</p><div class="buy"><div class="qty">1</div><div class="add">Add to cart</div></div></div>
  </div>
</main>
<footer class="footer">
  <div class="legal"><span>© 2015. Catapulta. All rights reserved.</span><span>Terms &amp; Condition</span><span>/</span><span>Privacy Policy</span></div>
  <div class="social"><span style="margin-right:4px">Connect with our social network :</span><span class="c" style="background:#2a5cb0"></span><span class="c" style="background:#3aa0e0"></span><span class="c" style="background:#333"></span><span class="c" style="background:#1f6e95"></span></div>
</footer>
</body>
</html>
```